Young, dynamic furniture company needs a new business card design

We require a new business card design for our modern furniture company which supplies furniture and appliances to the property and development market.
Fernmoor Furnishing has become one of the leading furniture & appliance suppliers to the property market withing London. With over 10 years experience, we have increased our business to supply not only private landlords and managing agents, but also property developers, housing associations and local councils.
We offer not only a complete range of furniture which includes beds, wardrobes, dining sets and sofas, but also a high quality, full delivery and assembly service to help you with all our furnishing needs.

Target Market(s)

Private landlords, estate agents, letting agents, property management companies

Industry/Entity Type

Business

Contact Information for Business Card

Name,
Title,
Address,
Mobile,
Telephone,
Fax, Website, email address

Font styles to use
Sans Serif

Colors
3176b5
0555a3
85abd2
cfdeed

Requirements
Must have
• All the above information for each of our staff, along with our logo

```html
<!DOCTYPE html>
<html lang="en">
<head>
<meta charset="utf-8">
<title>Fernmoor Furnishing – Business Card</title>
<link rel="stylesheet" href="https://fonts.googleapis.com/css2?family=Lato:wght@400;700&family=Montserrat:wght@500;700&display=swap">
<style>
  :root {
    --navy: #1f3d63;
    --navy-deep: #173150;
    --paper: #f7f8f9;
    --panel: #e9ebee;
    --ink: #2b2f36;
    --ink-soft: #555b64;
    --backdrop: #d9dcdf;
  }
  * { box-sizing: border-box; margin: 0; padding: 0; }
  html, body { width: 1200px; height: 800px; overflow: hidden; }
  body {
    background: var(--backdrop);
    font-family: "Lato", sans-serif;
    color: var(--ink);
    position: relative;
  }
  .card {
    position: absolute;
    width: 525px;
    height: 300px;
    background: var(--paper);
    box-shadow: 0 6px 18px rgba(0,0,0,0.18);
    overflow: hidden;
  }

  /* Back of card */
  .card-back { left: 575px; top: 80px; }
  .card-back .side-panel {
    position: absolute; top: 0; height: 222px;
    background: var(--panel);
  }
  .card-back .side-left { left: 0; width: 62px; }
  .card-back .side-right { right: 0; width: 78px; }
  .card-back .base-band {
    position: absolute; left: 0; right: 0; bottom: 0; height: 78px;
    background: linear-gradient(90deg, var(--navy) 0%, #2a4c75 55%, var(--navy-deep) 100%);
  }
  .brand {
    position: absolute;
    display: flex; flex-direction: column; align-items: center;
  }
  .card-back .brand { left: 0; right: 0; top: 62px; }
  .brand-mark {
    width: 26px; height: 26px; background: var(--navy); margin-bottom: 12px;
  }
  .brand-name {
    font-family: "Montserrat", sans-serif;
    font-weight: 500; color: var(--ink);
    text-transform: uppercase; letter-spacing: 0.02em;
    white-space: nowrap;
  }
  .card-back .brand-name { font-size: 17px; }
  .brand-tagline {
    font-family: "Montserrat", sans-serif;
    font-weight: 500; color: var(--ink-soft);
    text-transform: uppercase; letter-spacing: 0.08em;
    white-space: nowrap;
  }
  .card-back .brand-tagline { font-size: 8px; margin-top: 3px; }

  /* Front of card */
  .card-front { left: 100px; top: 420px; }
  .card-front .top-strip {
    position: absolute; left: 0; top: 0; width: 270px; height: 10px; background: var(--navy);
  }
  .card-front .logo-area {
    position: absolute; left: 0; top: 10px; width: 270px; height: 148px; background: #fbfbfc;
  }
  .card-front .brand { left: 0; right: 0; top: 34px; }
  .card-front .brand-mark { width: 22px; height: 22px; margin-bottom: 10px; }
  .card-front .brand-name { font-size: 14px; }
  .card-front .brand-tagline { font-size: 6.5px; margin-top: 3px; }
  .card-front .navy-block {
    position: absolute; left: 0; top: 158px; width: 270px; bottom: 0;
    background: linear-gradient(180deg, var(--navy) 0%, var(--navy-deep) 100%);
  }
  .card-front .info-panel {
    position: absolute; left: 270px; top: 0; right: 0; bottom: 0;
    background: var(--panel);
    padding: 38px 28px 0 28px;
  }
  .card-front .edge-tab {
    position: absolute; right: 0; top: 72px; width: 16px; height: 30px;
    background: var(--navy); border-radius: 3px 0 0 3px;
  }
  .person-name {
    font-family: "Montserrat", sans-serif;
    font-weight: 700; font-size: 17px; letter-spacing: 0.06em;
    color: var(--ink); text-transform: uppercase;
  }
  .person-title {
    font-family: "Montserrat", sans-serif;
    font-weight: 500; font-size: 11px; letter-spacing: 0.12em;
    color: var(--ink-soft); text-transform: uppercase;
  }
  .divider {
    width: 170px; height: 1px; background: var(--navy); margin: 6px 0 12px;
  }
  .contact-row {
    display: flex; align-items: flex-start; gap: 14px; margin-bottom: 8px;
  }
  .contact-icon {
    width: 17px; height: 17px; border-radius: 3px; background: var(--navy);
    flex: none; display: flex; align-items: center; justify-content: center;
  }
  .contact-lines {
    font-size: 11px; line-height: 12px; color: var(--ink); letter-spacing: 0.02em;
  }
</style>
</head>
<body>

<section class="card card-back" aria-label="Business card, back">
  <div class="side-panel side-left"></div>
  <div class="side-panel side-right"></div>
  <div class="brand">
    <div class="brand-mark"></div>
    <div class="brand-name">Fernmoor Furnishing</div>
    <div class="brand-tagline">Trade Furniture Solutions</div>
  </div>
  <div class="base-band"></div>
</section>

<section class="card card-front" aria-label="Business card, front">
  <div class="top-strip"></div>
  <div class="logo-area">
    <div class="brand">
      <div class="brand-mark"></div>
      <div class="brand-name">Fernmoor Furnishing</div>
      <div class="brand-tagline">Trade Furniture Solutions</div>
    </div>
  </div>
  <div class="navy-block"></div>

  <div class="info-panel">
    <div class="person-name">John Smith</div>
    <div class="person-title">Manager</div>
    <div class="divider"></div>

    <div class="contact-row">
      <span class="contact-icon">
        <svg width="11" height="11" viewBox="0 0 24 24" aria-hidden="true"><path fill="#fff" d="M6.6 10.8a15.1 15.1 0 0 0 6.6 6.6l2.2-2.2a1 1 0 0 1 1-.25 11.4 11.4 0 0 0 3.6.57 1 1 0 0 1 1 1V20a1 1 0 0 1-1 1A17 17 0 0 1 3 4a1 1 0 0 1 1-1h3.5a1 1 0 0 1 1 1c0 1.25.2 2.45.57 3.57a1 1 0 0 1-.25 1z"/></svg>
      </span>
      <div class="contact-lines">123 456 789<br>123 456 789<br>123 456 789</div>
    </div>

    <div class="contact-row">
      <span class="contact-icon">
        <svg width="11" height="11" viewBox="0 0 24 24" aria-hidden="true"><circle cx="12" cy="12" r="9" fill="none" stroke="#fff" stroke-width="2"/><path d="M3 12h18M12 3c3 3 3 15 0 18M12 3c-3 3-3 15 0 18" fill="none" stroke="#fff" stroke-width="1.6"/></svg>
      </span>
      <div class="contact-lines">john@website.com<br>www.website.com</div>
    </div>

    <div class="contact-row">
      <span class="contact-icon">
        <svg width="11" height="11" viewBox="0 0 24 24" aria-hidden="true"><path fill="#fff" d="M12 3 2 12h3v8h5v-5h4v5h5v-8h3z"/></svg>
      </span>
      <div class="contact-lines">Address Line 1<br>Address Line 2</div>
    </div>
  </div>
  <div class="edge-tab"></div>
</section>

</body>
</html>
```